KAZ Freightworks #ALLKAZ Business Cards & Letterhead

I am looking to business cards designed for our organization. We are currently undergoing a small re-branding that is taking place. Our organization is called KAZ Freightworks and we are headquartered in Phoenix, AZ. We primarily provide transportation and logistics services to the Meridel Parcel Bureau who is our largest customer. I would like to see a design that incorporates name, title, contact info, website, and address (this will be different depending on the employee). I would also like to see some color on the business card using our logo colors or a variation. I would like our logo on the back of the business card with the website displayed. The final design should communicate that we are a next generation transportation operate that focuses on being driver-first, customer-centric, innovative, and sustainable.We would also like our #ALLKAZ catch phrase incorporated as well.
Updates

Decision maker traveling outside of the country until Monday, November 25th.

Target Market(s)

Transportation & Logistics

Industry/Entity Type

Trucking Company

Contact Information for Business Card

-First and Last Name
-Position Title
-Contact Phone
-Contact Email
-Physical Address

Font styles to use
Serif

Colors

Designer to choose colors to be used in the design.

Requirements
Must have
• -KAZ logo prominently displayed
• -#ALLKAZ catch phrase used
• -Some amount of color, design gradient, etc.
• -Logo on the back with website listed (https://www.kazfreightco.example)

```html
<!DOCTYPE html>
<html lang="en">
<head>
<meta charset="utf-8">
<title>KAZ Freightworks Stationery</title>
<link href="https://fonts.googleapis.com/css2?family=Lato:wght@400;700;900&family=Arimo:wght@400;700&display=swap" rel="stylesheet">
<style>
  :root {
    --navy: #163a45;
    --green: #7bbd42;
    --paper: #f5f5f5;
    --ink: #1d1d1d;
    --backdrop: #dfdfe0;
  }
  * { margin: 0; padding: 0; box-sizing: border-box; }
  html, body { width: 1200px; height: 1200px; overflow: hidden; }
  body {
    background: radial-gradient(circle at 50% 55%, #e9eaeb 0%, var(--backdrop) 75%);
    position: relative;
    font-family: "Lato", sans-serif;
  }
  .sheet {
    position: absolute; background: var(--paper);
    box-shadow: 2px 3px 6px rgba(0,0,0,.28);
  }
  .letterhead { left: 102px; top: 164px; width: 669px; height: 863px; }
  .brand-name {
    position: absolute;
    display: flex; align-items: center; justify-content: center;
    font-family: "Lato", sans-serif; font-weight: 900; color: var(--navy);
    letter-spacing: 1px; line-height: 1;
  }
  .letterhead .brand-name { left: 52px; top: 39px; width: 95px; height: 95px; font-size: 36px; }
  .sender {
    position: absolute; left: 430px; top: 47px;
    font-size: 9.4px; line-height: 12px; color: var(--navy);
  }
  .sender .company { font-weight: 700; }
  .sender .contacts { margin-top: 6px; }
  .contact-line { display: flex; align-items: center; gap: 3px; }
  .contact-line svg { width: 8px; height: 8px; flex: none; }
  .letter {
    position: absolute; left: 52px; top: 220px; width: 576px;
    font-family: "Arimo", sans-serif; font-size: 9.6px; line-height: 13px; color: var(--ink);
  }
  .letter .recipient { margin-top: 13px; }
  .letter .salutation { margin-top: 27px; font-weight: 700; }
  .letter .body p { margin-top: 13px; text-align: justify; }
  .letter .body p:first-child { margin-top: 26px; }
  .letter .closing { margin-top: 39px; }
  .signature-area {
    margin-top: 14px; width: 134px; height: 20px;
    background: linear-gradient(90deg, #d9d9d9, #ececec);
    border-radius: 3px;
  }
  .letter .signer { margin-top: 10px; }
  .footer-band {
    position: absolute; left: 0; bottom: 0; width: 100%; height: 22px;
    background: var(--green);
  }
  .footer-band .navy-part {
    position: absolute; left: 0; top: 0; height: 100%; width: 422px;
    background: var(--navy);
    clip-path: polygon(0 0, 100% 0, calc(100% - 8px) 100%, 0 100%);
  }
  .footer-band .tag {
    position: absolute; left: 52px; top: 4px; font-size: 11px; color: #fff; font-weight: 400;
  }
  .tag .hash { color: var(--green); }

  .card { width: 276px; height: 157px; left: 822px; }
  .card-back { top: 286px; background: var(--navy); }
  .card-back .brand-name {
    left: 101px; top: 41px; width: 74px; height: 74px; font-size: 28px; color: #fff;
  }
  .card-back .site {
    position: absolute; left: 0; width: 100%; top: 132px; text-align: center;
    font-size: 7.2px; color: #fff; letter-spacing: .6px;
  }
  .card-back .site .mid { color: var(--green); }

  .card-front { top: 466px; }
  .card-front .brand-name { left: 25px; top: 20px; width: 57px; height: 57px; font-size: 22px; }
  .card-front .tag { position: absolute; left: 35px; top: 128px; font-size: 7.5px; color: var(--navy); }
  .holder { position: absolute; left: 106px; top: 37px; color: var(--navy); }
  .holder .name { font-size: 9.2px; font-weight: 700; color: var(--green); letter-spacing: .3px; }
  .holder .title { font-size: 7.4px; line-height: 9px; }
  .holder .rule { width: 19px; height: 1px; background: var(--green); margin: 10px 0 14px; }
  .holder .company { font-size: 7.2px; font-weight: 700; line-height: 9px; }
  .holder .address { font-size: 7px; line-height: 9px; }
  .holder .contacts { margin-top: 6px; font-size: 7px; line-height: 9px; }
  .holder .contact-line svg { width: 6px; height: 6px; }
  .card-front .footer-band { height: 7px; }
  .card-front .footer-band .navy-part { width: 102px; clip-path: polygon(0 0, 100% 0, calc(100% - 3px) 100%, 0 100%); }
</style>
</head>
<body>

<svg width="0" height="0" style="position:absolute">
  <defs>
    <symbol id="icon-phone" viewBox="0 0 16 16"><path fill="#7bbd42" d="M3.6 1.2l2.3 2.6-1.3 1.8c.9 2 2.5 3.6 4.6 4.6l1.8-1.3 2.6 2.3-1.2 2.4C7 13.4 2.6 9 1.2 3.6z"/></symbol>
    <symbol id="icon-mail" viewBox="0 0 16 16"><rect x="1" y="3" width="14" height="10" fill="none" stroke="#7bbd42" stroke-width="1.6"/><path d="M1 3l7 6 7-6" fill="none" stroke="#7bbd42" stroke-width="1.6"/></symbol>
    <symbol id="icon-globe" viewBox="0 0 16 16"><g fill="none" stroke="#7bbd42" stroke-width="1.2"><circle cx="8" cy="8" r="6.5"/><ellipse cx="8" cy="8" rx="3" ry="6.5"/><path d="M1.5 8h13M2.5 4.8h11M2.5 11.2h11"/></g></symbol>
  </defs>
</svg>

<section class="sheet letterhead">
  <div class="brand-name">KAZ</div>

  <div class="sender">
    <div class="company">KAZ Freightworks &amp; Energy Services, Inc.</div>
    <div>4410 North Canyon Ridge Road</div>
    <div>Glendale, AZ 85301</div>
    <div class="contacts">
      <div class="contact-line"><svg><use href="#icon-phone"/></svg>623-555-0148</div>
      <div class="contact-line"><svg><use href="#icon-mail"/></svg>info@kazfreightco.example</div>
      <div class="contact-line"><svg><use href="#icon-globe"/></svg>www.kazfreightco.example</div>
    </div>
  </div>

  <div class="letter">
    <div class="date">November 15, 2019</div>
    <div class="recipient">
      Mr. John Doe<br>President<br>AA Corporation<br>111 Street Name, Suite#<br>City, State, 12345
    </div>
    <div class="salutation">Dear Mr. John,</div>
    <div class="body">
      <p>Lorem ipsum dolor sit amet, consectetur adipiscing elit. Integer diam quam, egestas eu ultrices eu, suscipit ac sapien. Phasellus eu dui nisi. Nam et euismod diam, nec lobortis tortor. Donec et diam nulla. Aenean varius tincidunt convallis. Aliquam a tortor at lacus dictum aliquet. Nunc laoreet metus sapien, in scelerisque augue consectetur in.</p>
      <p>Fusce nec justo laoreet, egestas justo sed, aliquet sem. Pellentesque pharetra massa non orci bibendum semper. Pellentesque cursus eu lectus a consectetur. Nunc volutpat suscipit posuere. Vestibulum facilisis vel quam malesuada mattis. Nulla in mattis tellus. Maecenas tristique mauris vitae pharetra tincidunt. In ut ornare risus. Integer molestie vestibulum nisi, semper dapibus mi condimentum eu.</p>
      <p>Nullam sagittis elit libero, id fringilla est tincidunt eget. Donec in ipsum ultricies, consectetur quam vel, facilisis elit. Phasellus tincidunt congue risus vel luctus. Suspendisse ut mollis neque. Donec ornare orci in turpis vestibulum, in ultrices metus scelerisque. Pellentesque mattis mattis nunc, nec tincidunt lacus egestas id. Fusce facilisis sagittis neque sit amet vulputate. Aliquam ut eros lobortis tortor facilisis vehicula. Sed sed luctus leo, at laoreet sapien. Donec placerat adipiscing ligula non euismod. In lobortis pretium nisl id luctus.</p>
      <p>Integer gravida tincidunt nibh, scelerisque tincidunt turpis. Suspendisse potenti. Nunc hendrerit euismod lectus id elementum. Fusce vitae gravida velit, quis eleifend lectus. In imperdiet mauris eu dui viverra sagittis. Donec tempor dui diam, condimentum gravida lacus pretium a. Nullam fringilla augue quis arcu placerat scelerisque. Aliquam nec tincidunt augue, sit amet posuere ipsum.</p>
    </div>
    <div class="closing">Sincerely Yours,</div>
    <div class="signature-area" role="img" aria-label="Handwritten signature of Marlo Venter"></div>
    <div class="signer">Marlo Venter<br>President</div>
  </div>

  <div class="footer-band">
    <div class="navy-part"></div>
    <div class="tag"><span class="hash">#</span>ALLKAZ</div>
  </div>
</section>

<section class="sheet card card-back">
  <div class="brand-name">KAZ</div>
  <div class="site">www.<span class="mid">kazfreightco</span>.example</div>
</section>

<section class="sheet card card-front">
  <div class="brand-name">KAZ</div>
  <div class="tag"><span class="hash">#</span>ALLKAZ</div>
  <div class="holder">
    <div class="name">MARLO VENTER</div>
    <div class="title">President</div>
    <div class="rule"></div>
    <div class="company">KAZ Freightworks &amp; Energy Services, Inc.</div>
    <div class="address">4410 North Canyon Ridge Road<br>Glendale, AZ 85301</div>
    <div class="contacts">
      <div class="contact-line"><svg><use href="#icon-phone"/></svg>623-555-0148</div>
      <div class="contact-line"><svg><use href="#icon-mail"/></svg>marlo@kazfreightco.example</div>
      <div class="contact-line"><svg><use href="#icon-globe"/></svg>www.kazfreightco.example</div>
    </div>
  </div>
  <div class="footer-band"><div class="navy-part"></div></div>
</section>

</body>
</html>
```